Healthcare Information Interoperability Effort Needs a Roadmap Graphic

Interoperability of healthcare information is critical to accelerated research and improved patient outcomes. We are seeking a graphic to illustrate our roadmap for achieving healthcare information interoperability.

The roadmap has four key components. Please refer to this link for more information about direction and guide in the presentation.
https://lnkvyro.example/q7Zp3m

Industry/Entity Type

Healthcare

Font styles to use
Sans Serif

Requirements
Must have
• See https://lnkvyro.example/q7Zp3m
Nice to have

```html
<!DOCTYPE html>
<html lang="en">
<head>
<meta charset="utf-8">
<title>Healthcare Information Interoperability Roadmap</title>
<link rel="stylesheet" href="https://fonts.googleapis.com/css2?family=Arimo:wght@400&display=swap">
<style>
  :root {
    --bg: #ececec;
    --orange: #e3700d;
    --blue: #1b5a8f;
    --green: #95c11f;
    --hub: #cfcbca;
    --hub-text: #1d5a8c;
    --spark: #f08a2c;
    --white: #ffffff;
  }
  html, body {
    margin: 0;
    padding: 0;
    overflow: hidden;
    background: var(--bg);
  }
  .canvas {
    position: relative;
    width: 1200px;
    height: 1000px;
    background: var(--bg);
    font-family: "Arimo", Arial, sans-serif;
  }
  .roadmap { position: absolute; inset: 0; }
  .blade-orange { fill: var(--orange); }
  .blade-blue { fill: var(--blue); }
  .blade-green { fill: var(--green); }
  .hub { fill: var(--hub); }
  .blade-label {
    fill: var(--white);
    font-size: 35px;
  }
  .hub-title {
    fill: var(--hub-text);
    font-size: 27px;
  }
  .hub-sub {
    fill: var(--hub-text);
    font-size: 16px;
  }
  .flow-blue { fill: none; stroke: var(--blue); stroke-width: 20; }
  .flow-green { fill: none; stroke: var(--green); stroke-width: 20; }
  .head-blue { fill: var(--blue); }
  .head-green { fill: var(--green); }
  .spark { fill: var(--spark); }
  .graph-node { fill: var(--blue); }
  .graph-edge { stroke: var(--blue); stroke-width: 4; }
  .health-mark { fill: var(--blue); }
</style>
</head>
<body>
<div class="canvas">
  <svg class="roadmap" width="1200" height="1000" viewBox="0 0 1200 1000" xmlns="http://www.w3.org/2000/svg">
    <!-- Cycle blades -->
    <path class="blade-orange" d="M363,338 C380,200 450,70 560,50 C720,30 880,250 978,475 C860,330 700,240 560,240 C480,240 420,290 363,338 Z"/>
    <path class="blade-blue" d="M365,218 C250,360 150,520 165,660 C180,800 300,870 420,850 C470,845 520,835 553,823 C430,760 330,680 320,540 C310,420 330,300 365,218 Z"/>
    <path class="blade-green" d="M878,413 C980,500 1050,600 1035,720 C1020,830 920,895 780,895 C650,895 540,890 450,880 C620,840 760,780 830,680 C880,600 890,500 878,413 Z"/>

    <text class="blade-label" x="496" y="165">incentivize</text>
    <text class="blade-label" x="496" y="212">interoperability</text>
    <text class="blade-label" x="204" y="744">standardize</text>
    <text class="blade-label" x="204" y="791">the standards</text>
    <text class="blade-label" x="785" y="759">crowdsource</text>
    <text class="blade-label" x="785" y="806">mappings</text>

    <!-- Central goal -->
    <ellipse class="hub" cx="592" cy="415" rx="175" ry="107"/>
    <rect class="health-mark" x="578" y="320" width="26" height="44" rx="6" role="img" aria-label="Small healthcare emblem"/>
    <text class="hub-title" x="589" y="408" text-anchor="middle">Healthcare information</text>
    <text class="hub-title" x="589" y="444" text-anchor="middle">Interoperability</text>

    <!-- Foundation -->
    <ellipse class="hub" cx="601" cy="686" rx="137" ry="78"/>
    <text class="hub-sub" x="600" y="666" text-anchor="middle">RDF as a Universal</text>
    <text class="hub-sub" x="600" y="690" text-anchor="middle">information Representation</text>
    <g class="rdf-icon">
      <line class="graph-edge" x1="600" y1="722" x2="600" y2="745"/>
      <line class="graph-edge" x1="600" y1="722" x2="582" y2="733"/>
      <line class="graph-edge" x1="582" y1="733" x2="600" y2="745"/>
      <line class="graph-edge" x1="600" y1="745" x2="612" y2="748"/>
      <circle class="graph-node" cx="600" cy="722" r="6"/>
      <circle class="graph-node" cx="581" cy="734" r="7"/>
      <circle class="graph-node" cx="600" cy="745" r="6"/>
      <circle class="graph-node" cx="613" cy="748" r="5"/>
    </g>

    <!-- Flow arrows -->
    <path class="flow-blue" d="M478,637 C425,642 395,590 430,540"/>
    <polygon class="head-blue" points="420,498 470,510 440,550"/>
    <path class="flow-green" d="M722,637 C775,642 805,590 770,540"/>
    <polygon class="head-green" points="780,498 730,510 760,550"/>
    <polygon class="spark" points="608,522 626,544 617,544 620,560 611,566 614,584 606,584 602,606 597,582 603,582 598,562 607,556 601,544 592,544"/>
  </svg>
</div>
</body>
</html>
```